Letterhead and envelope design

Using current logo and colours I would like to have a new design done for a stationary set to be printed.

The new files should include logo, web and email address as well as,mailing address and phone number

Rory Vantosh
Vantosh Building Inc
Box 27 Site 18 RR5
Halvern Ridge ON
T4M 2B7
Cell : 555-201-2917
Email: rory@vantoshbuilding.example
web: vantoshbuilding.example

```html
<!DOCTYPE html>
<html lang="en">
<head>
<meta charset="utf-8">
<title>Vantosh Building – Letterhead</title>
<link href="https://fonts.googleapis.com/css2?family=Open+Sans:wght@400&family=Roboto:wght@400;500&display=swap" rel="stylesheet">
<style>
  :root {
    --navy: #0b2a5a;
    --orange: #d4780a;
    --ink: #555a60;
    --ink-dark: #2b2e33;
    --paper: #f8f8f8;
    --backdrop: #dcdcdc;
  }
  html, body {
    margin: 0;
    width: 1153px;
    height: 1200px;
    overflow: hidden;
    background: var(--backdrop);
  }
  .letterhead {
    position: absolute;
    left: 146px;
    top: 0;
    width: 860px;
    height: 1200px;
    background: var(--paper);
    overflow: hidden;
  }
  .brand {
    position: absolute;
    left: 78px;
    top: 67px;
    display: flex;
    align-items: center;
    gap: 16px;
  }
  .brand-dot {
    width: 116px;
    height: 116px;
    border-radius: 50%;
    background: var(--navy);
  }
  .brand-name {
    font-family: "Roboto", sans-serif;
    font-weight: 500;
    color: var(--navy);
    font-size: 26px;
    line-height: 30px;
    letter-spacing: 0.5px;
  }
  .contact {
    position: absolute;
    left: 568px;
    top: 74px;
    font-family: "Roboto", sans-serif;
    font-style: normal;
    font-size: 14.5px;
    line-height: 18px;
    color: var(--ink-dark);
  }
  .contact p { margin: 0; }
  .contact .address { margin-bottom: 6px; }
  .contact-line {
    display: flex;
    align-items: center;
    gap: 5px;
    line-height: 19px;
  }
  .contact-line svg { width: 13px; height: 13px; flex: none; }
  .letter {
    position: absolute;
    left: 78px;
    top: 298px;
    width: 705px;
    font-family: "Open Sans", sans-serif;
    font-size: 15.4px;
    line-height: 23.1px;
    color: var(--ink);
  }
  .letter p {
    margin: 0 0 23px;
    text-align: justify;
  }
  .signature {
    position: absolute;
    left: 78px;
    top: 908px;
    width: 102px;
    height: 94px;
    background: linear-gradient(135deg, #e6e6e6, #d2d2d2);
  }
  .footer-band {
    position: absolute;
    left: 0;
    bottom: 0;
    width: 860px;
    height: 20px;
  }
</style>
</head>
<body>
  <main class="letterhead">
    <header>
      <div class="brand">
        <div class="brand-dot"></div>
        <div class="brand-name">VANTOSH<br>BUILDING</div>
      </div>
      <address class="contact">
        <p class="address">Vantosh Building Inc<br>Box 27 Site 18 RR5<br>Halvern Ridge ON T4M 2B7</p>
        <p class="contact-line">
          <svg viewBox="0 0 13 13" aria-hidden="true"><rect x="3" y="0.5" width="7" height="12" rx="1.2" fill="none" stroke="var(--orange)" stroke-width="1.3"/><circle cx="6.5" cy="10.2" r="0.8" fill="var(--orange)"/></svg>
          555-201-2917
        </p>
        <p class="contact-line">
          <svg viewBox="0 0 13 13" aria-hidden="true"><rect x="0.5" y="2.5" width="12" height="8" fill="var(--orange)"/><path d="M0.5 2.5 L6.5 7 L12.5 2.5" fill="none" stroke="#fff" stroke-width="1"/></svg>
          rory@vantoshbuilding.example
        </p>
        <p class="contact-line">
          <svg viewBox="0 0 13 13" aria-hidden="true"><circle cx="6.5" cy="6.5" r="6" fill="var(--orange)"/><path d="M6.5 0.5 V12.5 M0.5 6.5 H12.5" stroke="#fff" stroke-width="0.9"/></svg>
          www.vantoshbuilding.example
        </p>
      </address>
    </header>

    <section class="letter">
      <p>Dear customer,</p>
      <p>Lorem ipsum dolor sit amet, consectetur adipisicing elit, sed do eiusmod tempor incididunt ut labore et dolore magna aliqua. Ut enim ad minim veniam, quis nostrud exercitation ullamco laboris nisi ut aliquip ex ea commodo consequat. Duis aute irure dolor in reprehenderit in voluptate velit esse cillum dolore eu fugiat nulla pariatur. Excepteur sint occaecat cupidatat non proident, sunt in culpa qui officia deserunt mollit anim id est laborum.</p>
      <p>Lorem ipsum dolor sit amet, consectetur adipisicing elit, sed do eiusmod tempor incididunt ut labore et dolore magna aliqua. Ut enim ad minim veniam, quis nostrud exercitation ullamco laboris nisi ut aliquip ex ea commodo consequat. Duis aute irure dolor in reprehenderit in voluptate velit esse cillum dolore eu fugiat nulla pariatur. Excepteur sint occaecat cupidatat non proident, sunt in culpa qui officia deserunt mollit anim id est laborum.</p>
      <p>Lorem ipsum dolor sit amet, consectetur adipisicing elit, sed do eiusmod tempor incididunt ut labore et dolore magna aliqua. Ut enim ad minim veniam, quis nostrud exercitation ullamco laboris nisi ut aliquip ex ea commodo consequat. Duis aute irure dolor in reprehenderit in voluptate velit esse cillum dolore eu fugiat nulla pariatur. Excepteur sint occaecat cupidatat non proident, sunt in culpa qui officia deserunt mollit anim id est laborum.</p>
      <p>Lorem ipsum dolor sit amet, consectetur adipisicing elit, sed do eiusmod tempor incididunt ut labore et dolore magna aliqua. Ut enim ad minim veniam, quis nostrud exercitation ullamco laboris nisi ut aliquip ex ea commodo consequat. Duis aute irure dolor in reprehenderit.</p>
      <p>Yours Sincerely,</p>
    </section>

    <div class="signature" role="img" aria-label="Handwritten signature of the sender"></div>

    <svg class="footer-band" viewBox="0 0 860 20" preserveAspectRatio="none" aria-hidden="true">
      <polygon points="0,0 676,0 656,20 0,20" fill="var(--navy)"/>
      <polygon points="680,0 860,0 860,20 660,20" fill="#ffffff"/>
      <polygon points="699,0 860,0 860,20 679,20" fill="var(--orange)"/>
    </svg>
  </main>
</body>
</html>
```